Strong, modern, clean Business Card design

Looking for a stunning, but CLEAN business card design. While we are a faith-based organization, we do NOT want this to look religious.

Industry/Entity Type

Non-Profit

Contact Information for Business Card

Mark Dalton | Lead Pastor
mark@BraverHollow.org
555-218-9034
PO Box 7183
Alderton, CO 80000

Font styles to use
Serif
Sans Serif

Requirements
Should not have
• Religious imagery or symbolism

```html
<!DOCTYPE html>
<html lang="en">
<head>
<meta charset="utf-8">
<title>Braver Hollow — Business Card</title>
<link rel="stylesheet" href="https://fonts.googleapis.com/css2?family=Work+Sans:wght@400;600&display=swap">
<style>
  :root {
    --backdrop: #1c1c1c;
    --card: #262626;
    --card-edge: #4a7e97;
    --accent: #4f86a0;
    --ink: #f2f2f2;
  }
  * { margin: 0; padding: 0; box-sizing: border-box; }
  html, body {
    width: 1200px; height: 900px; overflow: hidden;
    background: var(--backdrop);
  }
  .canvas {
    position: relative; width: 1200px; height: 900px;
    font-family: "Work Sans", Arial, sans-serif;
  }
  .card {
    position: absolute; left: 220px; width: 760px; height: 380px;
    background: var(--card);
    border-bottom: 7px solid var(--card-edge);
    box-shadow: 0 10px 30px rgba(0,0,0,0.45);
  }
  .card--front { top: 50px; display: flex; align-items: center; justify-content: center; }
  .card--back { top: 470px; }

  .org-name {
    color: var(--accent);
    font-weight: 600;
    font-size: 64px;
    letter-spacing: 1px;
    margin-top: -40px;
  }

  .identity {
    position: absolute; right: 420px; top: 142px;
    text-align: right;
    color: var(--accent);
    font-weight: 600;
    font-size: 31px;
    line-height: 38px;
    text-transform: uppercase;
    letter-spacing: 0.5px;
  }
  .divider {
    position: absolute; left: 362px; top: 128px;
    width: 2px; height: 98px; background: var(--ink);
  }
  .contact {
    position: absolute; left: 392px; top: 134px;
    color: var(--ink); font-size: 17px; line-height: 24px;
    list-style: none; letter-spacing: 0.6px;
  }
  .contact li { display: flex; align-items: center; white-space: nowrap; }
  .contact .icon { width: 12px; height: 12px; margin-right: 12px; flex: none; }
</style>
</head>
<body>
<main class="canvas">
  <section class="card card--front">
    <div class="org-name">Braver Hollow</div>
  </section>

  <section class="card card--back">
    <div class="identity">
      <div class="identity__name">Mark Dalton</div>
      <div class="identity__role">Lead Pastor</div>
    </div>
    <div class="divider"></div>
    <ul class="contact">
      <li>PO Box 7183</li>
      <li>Alderton, CO 80000</li>
      <li>
        <svg class="icon" viewBox="0 0 12 12" aria-hidden="true">
          <path d="M2.5 1 L4.5 1 L5 3.5 L3.8 4.3 Q4.8 6.8 7.5 8.2 L8.3 7 L11 7.5 L11 9.5 Q10.5 11 9 11 Q2 10 1 3 Q1 1.5 2.5 1 Z" fill="var(--accent)"/>
        </svg>
        555-218-9034
      </li>
      <li>
        <svg class="icon" viewBox="0 0 12 12" aria-hidden="true">
          <rect x="0.75" y="2.25" width="10.5" height="7.5" fill="none" stroke="var(--accent)" stroke-width="1.3"/>
          <path d="M1 2.6 L6 6.6 L11 2.6" fill="none" stroke="var(--accent)" stroke-width="1.3"/>
        </svg>
        mark@BraverHollow.org
      </li>
    </ul>
  </section>
</main>
</body>
</html>
```